Website design in Wordpress for Golf Simulator Center

We are opening a new golf simulator center in Copenhagen, and need a website design. We are using wordpress, and our site is https://vornlo-tee.dk
We will need a design for the frontpage, and a design for subpages (which we will be reusing for all subpages).
Logo is as seen on the site, and our base color scheme is leaf green.
As text, take the text on the current website, or put some placeholder text in english.
Should be responsive and look good on both desktop and mobile.
Target Market(s)
Male, 18-60, golf players

```html
<!DOCTYPE html>
<html lang="en">
<head>
<meta charset="utf-8">
<title>Vornlo Tee – Golf Simulator</title>
<link rel="stylesheet" href="https://fonts.googleapis.com/css2?family=Oswald:wght@300;400;600;700&family=Poppins:wght@300;400;500&display=swap">
<style>
:root{
  --navy:#131c44;
  --navy-deep:#0e1636;
  --green:#0fa37f;
  --mint:#e7f6f2;
  --mint-field:#daf1ec;
  --white:#ffffff;
  --ink:#1d2447;
  --muted:#8a8fa5;
}
*{box-sizing:border-box;margin:0;padding:0}
html,body{width:1200px;height:2263px;overflow:hidden}
body{position:relative;background:var(--navy);font-family:'Poppins',sans-serif;color:var(--white)}
.abs{position:absolute}
.heading{font-family:'Oswald',sans-serif;font-weight:300;text-transform:uppercase;letter-spacing:1px;line-height:1.1}
.heading strong{font-weight:700}
.accent{color:var(--green)}

/* header */
.site-header{left:0;top:0;width:1200px;height:79px;background:var(--navy)}
.menu-toggle{left:44px;top:37px;width:17px;height:8px;border-top:2px solid #fff;border-bottom:2px solid #fff}
.nav-link{top:34px;font-size:12px;font-weight:400;letter-spacing:.2px}
.brand{left:502px;top:20px;width:200px;text-align:center;font-family:'Oswald',sans-serif;font-weight:600;font-size:30px;letter-spacing:1px;line-height:36px}

/* side social */
.side-social{left:46px;width:14px;height:14px;border-radius:50%;background:#3a4470}
.side-social.active{background:var(--green)}

/* hero */
.hero-photo{left:103px;top:79px;width:1097px;height:594px;background:linear-gradient(180deg,#1d2a33 0%,#2b4a3e 45%,#35612f 75%,#1c2a1c 100%)}
.hero-title{left:168px;top:436px;font-size:54px;color:#fff}
.hero-title strong{display:block;font-size:68px;margin-top:4px}

/* intro */
.intro-text{left:168px;top:724px;width:415px;font-size:13.2px;line-height:20.6px;font-weight:300}
.read-more{left:168px;top:845px;font-size:12.5px;font-weight:500;display:flex;align-items:center;gap:6px}
.divider{left:614px;top:712px;width:1px;height:164px;background:#3a4470}
.intro-heading{left:651px;top:733px;font-size:39px}
.intro-heading strong{display:block}

/* reception */
.reception-band{left:0;top:962px;width:1200px;height:570px;background:var(--mint)}
.bar-photo{left:169px;top:892px;width:416px;height:559px;background:linear-gradient(160deg,#d9c6a8 0%,#8a6a48 40%,#2a2a2a 75%,#1d3a22 100%)}
.reception-heading{left:627px;top:1066px;font-size:40px;color:var(--ink)}
.reception-text{left:629px;top:1128px;width:410px;font-size:13.2px;line-height:20.6px;color:var(--ink);font-weight:300}
.email-field{left:629px;top:1286px;width:273px;height:44px;background:var(--mint-field);font-size:10px;color:var(--ink);padding:16px 17px}
.email-button{left:902px;top:1286px;width:129px;height:44px;background:var(--green);color:#fff;font-size:12px;font-weight:500;text-align:center;line-height:44px}

/* membership */
.membership-band{left:0;top:1532px;width:1200px;height:404px;background:var(--navy-deep)}
.sim-photo{left:0;top:1532px;width:640px;height:404px;background:linear-gradient(90deg,#1b2a1f 0%,#3c6b35 40%,#2a4a3a 70%,rgba(14,22,54,1) 100%)}
.membership-heading{left:610px;top:1606px;font-size:40px}
.membership-sub{left:611px;top:1662px;font-family:'Oswald',sans-serif;font-weight:600;font-size:24px;color:var(--green);letter-spacing:.5px}
.benefits{left:611px;top:1705px;list-style:none}
.benefits li{display:flex;align-items:center;gap:8px;font-size:16.5px;font-weight:300;height:32.3px}
.benefits small{font-size:12.5px}

/* newsletter */
.newsletter-band{left:0;top:1936px;width:1200px;height:253px;background:#fff}
.newsletter-heading{left:0;top:2008px;width:1200px;text-align:center;font-size:40px;color:var(--ink)}
.field{top:2104px;height:29px;font-size:10.5px;color:var(--ink);border-bottom:1px solid #d6d9e0}
.field.focus{border-bottom:2px solid var(--green)}
.signup-button{left:804px;top:2090px;width:128px;height:44px;background:var(--green);color:#fff;font-size:12px;font-weight:500;text-align:center;line-height:44px}

/* footer */
.footer-brand{left:0;top:2189px;width:190px;height:74px;background:var(--green);font-family:'Oswald',sans-serif;font-weight:600;font-size:20px;letter-spacing:.5px;display:flex;align-items:center;justify-content:center}
.copyright{left:220px;top:2218px;font-size:11.5px;font-weight:300}
.footer-social{top:2218px;width:18px;height:18px;border-radius:50%;background:var(--green)}
</style>
</head>
<body>

<header class="abs site-header">
  <div class="abs menu-toggle"></div>
  <span class="abs nav-link" style="left:217px">HOME</span>
  <span class="abs nav-link" style="left:338px">GOLF SIMULATOR</span>
  <div class="abs brand">VORNLO TEE</div>
  <span class="abs nav-link" style="left:765px">RESOURECS</span>
  <span class="abs nav-link" style="left:922px">ABOUT US</span>
</header>

<div class="abs hero-photo" role="img" aria-label="Photo of a golfer swinging in front of a simulator screen showing shot data and a fairway, with a guest watching from an armchair"></div>
<h1 class="abs heading hero-title">State-of-the-art<strong>Technology</strong></h1>

<span class="abs side-social active" style="top:307px"></span>
<span class="abs side-social" style="top:349px"></span>
<span class="abs side-social" style="top:390px"></span>
<span class="abs side-social" style="top:430px"></span>

<p class="abs intro-text">In January 2023, a new golf simulator center will open in Valby with 8 simulators of the Swingtrak 4 type. We look forward to being able to welcome new and experienced golfers. With us, you can practice all kinds of shots indoors, sheltered from rain and snow, or play an entire 18-hole course in half the time.</p>
<a class="abs read-more">READ MORE
  <svg width="14" height="8" viewBox="0 0 14 8"><path d="M0 4h12M9 1l3 3-3 3" stroke="#fff" stroke-width="1.2" fill="none"/></svg>
</a>
<div class="abs divider"></div>
<h2 class="abs heading intro-heading">Golf simulator in Valby<strong>Opens January 2023</strong></h2>

<section class="abs reception-band"></section>
<div class="abs bar-photo" role="img" aria-label="Photo of the lounge bar with wood slat walls, glass shelves, a drinks fridge and a green counter"></div>
<h2 class="abs heading reception-heading">Opening <strong class="accent">Reception</strong></h2>
<p class="abs reception-text">We will hold an opening reception on 20 January 2023 from 4 p.m. More information will be available on this page continuously, and via our newsletter, which you can sign up for here. See also our Chatterly event . Stop by and try a few shots, get a free Friday beer or 2 and enter contests to win free spring season memberships and other prizes.</p>
<div class="abs email-field">Email Address:</div>
<div class="abs email-button">YES PLEASE!</div>

<section class="abs membership-band"></section>
<div class="abs sim-photo" role="img" aria-label="Photo of a golfer mid-swing beside a simulator screen showing a green fairway and clubhouse"></div>
<h2 class="abs heading membership-heading">Buy a starter <strong class="accent">Membership</strong></h2>
<div class="abs membership-sub">OPSTARTSMEDLEMSSKAB</div>
<ul class="abs benefits">
  <li><svg width="14" height="14" viewBox="0 0 14 14"><circle cx="7" cy="7" r="6" stroke="#0fa37f" stroke-width="1.2" fill="none"/><path d="M4 7l2 2 4-4" stroke="#0fa37f" stroke-width="1.3" fill="none"/></svg>Kan indloses fra vi abner <small>(sker senest 1. februar 2023)</small></li>
  <li><svg width="14" height="14" viewBox="0 0 14 14"><circle cx="7" cy="7" r="6" stroke="#0fa37f" stroke-width="1.2" fill="none"/><path d="M4 7l2 2 4-4" stroke="#0fa37f" stroke-width="1.3" fill="none"/></svg>Noglebrik inluderet: Adgang 08:00 till 23:00</li>
  <li><svg width="14" height="14" viewBox="0 0 14 14"><circle cx="7" cy="7" r="6" stroke="#0fa37f" stroke-width="1.2" fill="none"/><path d="M4 7l2 2 4-4" stroke="#0fa37f" stroke-width="1.3" fill="none"/></svg>5xl timers spil inkluderet</li>
  <li><svg width="14" height="14" viewBox="0 0 14 14"><circle cx="7" cy="7" r="6" stroke="#0fa37f" stroke-width="1.2" fill="none"/><path d="M4 7l2 2 4-4" stroke="#0fa37f" stroke-width="1.3" fill="none"/></svg>Bookinger til halv pris <small>(normalpris 400,-)</small></li>
  <li><svg width="14" height="14" viewBox="0 0 14 14"><circle cx="7" cy="7" r="6" stroke="#0fa37f" stroke-width="1.2" fill="none"/><path d="M4 7l2 2 4-4" stroke="#0fa37f" stroke-width="1.3" fill="none"/></svg>Gyldigt frem til 31. August 2023</li>
</ul>

<section class="abs newsletter-band"></section>
<h2 class="abs heading newsletter-heading">Newsletter <strong class="accent">Signup</strong></h2>
<div class="abs field focus" style="left:266px;width:254px">Name</div>
<div class="abs field" style="left:532px;width:255px">Email</div>
<div class="abs signup-button">SIGN UP</div>

<footer>
  <div class="abs footer-brand">VORNLO TEE</div>
  <p class="abs copyright">Copyright © 2023. <span class="accent">Vornlo Tee ApS.</span> All Received</p>
  <span class="abs footer-social" style="left:1031px"></span>
  <span class="abs footer-social" style="left:1072px"></span>
  <span class="abs footer-social" style="left:1112px"></span>
  <span class="abs footer-social" style="left:1154px"></span>
</footer>

</body>
</html>
```